Thornwell Building Company - advertisement poster

I am looking to print some canvas signs to advertise my general contracting company, Thornwell Building Company. The sign will measure 6' long x 3' high so the size should match that ratio. I already have a logo icon, which is the Letter 'A' and some trees that I would like to incorporate, see attached. I would also like the to have the following information listed:
1) phone number: 472-318-6095
2) email: thornwellbuildingcompany@mailvistra.net
3) website: thornwellbuildingcompany.com
4) Lic#5386204
5) I want to use this text: "BUILD WITH THE T-CREW!"

The ad should be relatively simple and clean. Black and Green are my company colors. I am open to creative ideas!

Target Market(s)

People looking to renovate their homes

Industry/Entity Type

Construction

Colors
59FF00
82FF00
B8FF75
E3FFCB
F4FFEA

Requirements
Must have
• Must have my company logo
Should not have
• No photos or complex graphics

```html
<!DOCTYPE html>
<html lang="en">
<head>
<meta charset="utf-8">
<title>Thornwell Building Company – Sign</title>
<link href="https://fonts.googleapis.com/css2?family=Montserrat:wght@400;600;700&family=Oswald:wght@700&display=swap" rel="stylesheet">
<style>
  :root {
    --backdrop: #262b2d;
    --ink: #07090b;
    --lime: #64e900;
    --white: #ffffff;
  }
  * { margin: 0; padding: 0; box-sizing: border-box; }
  html, body {
    width: 1200px; height: 676px; overflow: hidden;
    background: var(--backdrop);
    font-family: "Montserrat", sans-serif;
  }
  .sign {
    position: absolute; left: 0; top: 38px;
    width: 1200px; height: 600px;
    background: var(--ink);
    overflow: hidden;
  }
  .license {
    position: absolute; top: 18px; width: 100%;
    text-align: center; color: var(--lime);
    font-size: 17px; font-weight: 400; letter-spacing: 0.5px;
  }
  .brand-name {
    position: absolute; top: 150px; width: 100%;
    text-align: center; color: var(--white);
    font-weight: 700; font-size: 46px; line-height: 1.15;
    letter-spacing: 2px; text-transform: uppercase;
  }
  .brand-mark {
    position: absolute; top: 74px; left: 560px;
    width: 80px; height: 80px; border-radius: 50%;
    background: var(--lime);
  }
  .lime-field {
    position: absolute; left: 0; right: 0; top: 349px; bottom: 0;
    background: var(--lime);
    border-radius: 120px 120px 0 0;
  }
  .slogan {
    position: absolute; left: 340px; top: 312px;
    width: 520px; height: 67px;
    background: var(--ink);
    border: 3px solid var(--lime);
    border-radius: 34px;
    display: flex; align-items: center; justify-content: center;
    color: var(--white);
    font-family: "Oswald", sans-serif; font-weight: 700;
    font-size: 42px; letter-spacing: 1.5px;
  }
  .contact {
    position: absolute; top: 408px; width: 100%;
    text-align: center;
  }
  .contact-cta {
    color: var(--white); font-weight: 700; font-size: 20px; letter-spacing: 0.5px;
  }
  .contact-phone {
    color: var(--ink); font-weight: 700; font-size: 52px; line-height: 1.1; margin-top: 2px;
  }
  .contact-line {
    display: flex; align-items: center; justify-content: center; gap: 8px;
    color: var(--white); font-size: 21px; font-weight: 400; margin-top: 6px;
  }
  .contact-line svg { width: 22px; height: 22px; flex: none; }
</style>
</head>
<body>
  <main class="sign">
    <p class="license">Lic#5386204</p>
    <div class="brand-mark"></div>
    <h1 class="brand-name">Thornwell<br>Building Company</h1>
    <div class="lime-field"></div>
    <p class="slogan">BUILD WITH THE T-CREW!</p>
    <section class="contact">
      <p class="contact-cta">CONTACT US NOW!</p>
      <p class="contact-phone">472-318-6095</p>
      <p class="contact-line">
        <svg viewBox="0 0 24 24" fill="none" stroke="#fff" stroke-width="1.6"><rect x="2" y="5" width="20" height="14" rx="2"/><path d="M2.5 6l9.5 7 9.5-7"/></svg>
        thornwellbuildingcompany@mailvistra.net
      </p>
      <p class="contact-line">
        <svg viewBox="0 0 24 24" fill="none" stroke="#fff" stroke-width="1.6"><circle cx="12" cy="12" r="10"/><ellipse cx="12" cy="12" rx="4.5" ry="10"/><path d="M2 12h20"/></svg>
        thornwellbuildingcompany.com
      </p>
    </section>
  </main>
</body>
</html>
```